Elegant and Professional Business card design needed

The patron journey mentor is a company which provides consulting services to businesses to assist them in improving the customer experience for their customers.

I need a business card design which tells people I'm there to help them.

Target Market(s)

Small to medium business owners

Industry/Entity Type

Business

Contact Information for Business Card

Martin Glenholme
The Patron Journey Mentor
Web: http://www.ThePatronJourneyMentor.example
Email: martin@ThePatronJourneyMentor.example
Phone: +61 400 582316

Logo styles of interest
Abstract Logo
Requirements
Must have
• Some sort of image / graphic representing the customer is important and should be at the heart of a business.

```html
<!DOCTYPE html>
<html lang="en">
<head>
<meta charset="utf-8">
<title>The Patron Journey Mentor – Business Card</title>
<link rel="stylesheet" href="https://fonts.googleapis.com/css2?family=Didact+Gothic&display=swap">
<style>
  :root {
    --backdrop: #e4e4e4;
    --card-white: #ffffff;
    --charcoal: #2c2f31;
    --charcoal-deep: #232527;
    --ink: #2a2a2a;
    --orange: #ec6a26;
    --rock-light: #6b6e70;
    --rock-dark: #3a3c3e;
    --text-light: #f4f4f4;
  }
  * { margin: 0; padding: 0; box-sizing: border-box; }
  html, body {
    width: 1200px;
    height: 900px;
    overflow: hidden;
    background: var(--backdrop);
    font-family: "Didact Gothic", "Century Gothic", sans-serif;
  }
  .card {
    position: absolute;
    left: 100px;
    top: 160px;
    width: 1000px;
    height: 580px;
    border-radius: 44px;
    overflow: hidden;
    background: var(--charcoal);
    box-shadow: 0 10px 30px rgba(0,0,0,0.18);
  }
  .card__bands {
    position: absolute;
    inset: 0;
  }
  .card__illustration {
    position: absolute;
    right: 0;
    top: 0;
    width: 300px;
    height: 232px;
    background: linear-gradient(160deg, var(--card-white) 0%, var(--rock-light) 45%, var(--rock-dark) 100%);
  }
  .card__company {
    position: absolute;
    left: 44px;
    top: 140px;
    font-size: 58px;
    line-height: 1;
    color: var(--ink);
    letter-spacing: -0.5px;
    white-space: nowrap;
  }
  .card__name {
    position: absolute;
    left: 58px;
    top: 262px;
    font-size: 40px;
    color: var(--orange);
  }
  .contact-list {
    position: absolute;
    left: 56px;
    top: 388px;
    list-style: none;
  }
  .contact-list__item {
    display: flex;
    align-items: center;
    gap: 12px;
    height: 50px;
    color: var(--text-light);
    font-size: 33px;
    white-space: nowrap;
  }
  .contact-list__item--phone { font-size: 40px; }
  .contact-icon {
    width: 38px;
    height: 38px;
    flex: none;
  }
</style>
</head>
<body>
  <main class="card">
    <svg class="card__bands" viewBox="0 0 1000 580" aria-hidden="true">
      <polygon points="0,0 1000,0 1000,190 0,212" fill="var(--card-white)"/>
      <polygon points="0,212 1000,190 1000,205 0,229" fill="var(--orange)"/>
    </svg>

    <div class="card__illustration" role="img" aria-label="Illustration of two climbers helping each other up a dark rocky peak"></div>

    <h1 class="card__company">The Patron Journey Mentor</h1>

    <p class="card__name">Martin Glenholme</p>

    <ul class="contact-list">
      <li class="contact-list__item contact-list__item--phone">
        <svg class="contact-icon" viewBox="0 0 40 40" aria-label="Phone">
          <rect x="2" y="2" width="36" height="36" rx="6" fill="var(--orange)"/>
          <path d="M9 16c0-5 5-7 11-7s11 2 11 7l-5 1-1-4c-3-1-7-1-10 0l-1 4z" fill="var(--charcoal)"/>
          <path d="M12 20h16l3 11H9z" fill="var(--charcoal)"/>
          <circle cx="20" cy="25" r="3" fill="var(--orange)"/>
        </svg>
        <span>+61 400 582316</span>
      </li>
      <li class="contact-list__item">
        <svg class="contact-icon" viewBox="0 0 40 40" aria-label="Email">
          <rect x="3" y="8" width="34" height="24" rx="2" fill="var(--orange)"/>
          <path d="M4 10l16 12 16-12" fill="none" stroke="var(--charcoal)" stroke-width="2.5"/>
        </svg>
        <span>martin@ThePatronJourneyMentor.example</span>
      </li>
      <li class="contact-list__item">
        <svg class="contact-icon" viewBox="0 0 40 40" aria-label="Website">
          <circle cx="20" cy="20" r="17" fill="var(--orange)"/>
          <g fill="none" stroke="var(--charcoal)" stroke-width="2">
            <ellipse cx="20" cy="20" rx="7" ry="17"/>
            <line x1="3" y1="20" x2="37" y2="20"/>
            <path d="M6 11h28M6 29h28"/>
            <line x1="20" y1="3" x2="20" y2="37"/>
          </g>
        </svg>
        <span>www.ThePatronJourneyMentor.example</span>
      </li>
    </ul>
  </main>
</body>
</html>
```